Brennick Holdings Business Cards

These are professional business cards that are for my family office.
Put fake emails and phone numbers as of now until I finalize those components. This family office controls my families investments, assets, and future. The cards should be professional.
..
.
.
.
I just uploaded another variation of a logo I would like to see as a business card to I am inbeteen which logo to use

Target Market(s)

business

Industry/Entity Type

business

Contact Information for Business Card

Professional, wealth related, finance related.

Requirements
Must have
• Logo

```html
<!DOCTYPE html>
<html lang="en">
<head>
<meta charset="utf-8">
<title>Brennick Holdings Business Cards</title>
<link href="https://fonts.googleapis.com/css2?family=Roboto:wght@400;500&display=swap" rel="stylesheet">
<style>
  :root {
    --backdrop: #bdbebf;
    --card-light: #f2f2f4;
    --ink-navy: #1c2230;
    --ink-grey: #555a60;
    --rule-grey: #a9abae;
    --dot-grey: #a6a7a9;
    --back-top: #1b2030;
    --back-bottom: #0d1119;
    --back-ink: #ffffff;
  }
  html, body {
    margin: 0;
    padding: 0;
    width: 1200px;
    height: 1000px;
    overflow: hidden;
    background: var(--backdrop);
    font-family: "Roboto", Arial, sans-serif;
  }
  .canvas { position: relative; width: 1200px; height: 1000px; }
  .card-front {
    position: absolute;
    left: 299px; top: 143px;
    width: 602px; height: 344px;
    background: var(--card-light);
  }
  .wordmark {
    position: absolute;
    left: 0; right: 0; top: 66px;
    margin: 0;
    text-align: center;
    font-family: "Roboto", Arial, sans-serif;
    font-weight: 500;
    font-size: 46px;
    line-height: 54px;
    letter-spacing: 1px;
    color: var(--ink-navy);
  }
  .holder { position: absolute; left: 83px; top: 176px; }
  .holder-name {
    margin: 0;
    font-weight: 500;
    font-size: 16.5px;
    letter-spacing: 0.3px;
    color: var(--ink-navy);
    line-height: 20px;
  }
  .holder-role { margin: 0; font-size: 14.5px; color: var(--ink-grey); line-height: 18px; }
  .contact {
    position: absolute;
    left: 325px; top: 175px;
    font-size: 14.5px;
    color: var(--ink-grey);
    line-height: 18px;
  }
  .address { margin: 0 0 10px; font-style: normal; }
  .contact-line { display: flex; align-items: center; gap: 7px; height: 20px; }
  .contact-line svg { width: 14px; height: 12px; fill: var(--ink-navy); }
  .web-rule {
    position: absolute;
    left: 83px; right: 0; top: 288px;
    display: flex;
    align-items: center;
    font-size: 14.5px;
    color: var(--ink-grey);
  }
  .web-rule .bullets { display: flex; gap: 3px; }
  .web-rule .bullets i {
    display: block; width: 8px; height: 8px;
    border-radius: 50%; background: var(--dot-grey);
  }
  .web-rule .rule { height: 1px; background: var(--rule-grey); }
  .web-rule .rule-left { width: 176px; margin-right: 4px; }
  .web-rule .rule-right { flex: 1; margin-left: 5px; }
  .web-rule strong { font-weight: 400; color: var(--ink-navy); }
  .card-back {
    position: absolute;
    left: 299px; top: 513px;
    width: 602px; height: 343px;
    background: linear-gradient(160deg, var(--back-top), var(--back-bottom));
  }
  .back-pattern { position: absolute; inset: 0; }
  .back-brand {
    position: absolute;
    left: 0; right: 0; top: 150px;
    display: flex;
    justify-content: center;
    align-items: center;
    gap: 14px;
    color: var(--back-ink);
    font-weight: 500;
    font-size: 30px;
    letter-spacing: 1px;
    line-height: 40px;
  }
  .back-brand .ring {
    width: 34px; height: 34px;
    border: 2px solid var(--back-ink);
    border-radius: 50%;
    box-sizing: border-box;
  }
</style>
</head>
<body>
<main class="canvas">
  <section class="card-front">
    <h1 class="wordmark">Brennick Holdings</h1>
    <div class="holder">
      <p class="holder-name">DANIEL HARTWELL</p>
      <p class="holder-role">Managing Director</p>
    </div>
    <div class="contact">
      <address class="address">480 Marlowe Ave Suite 210<br>Carver Bay<br>90412 California / USA</address>
      <div class="contact-line">
        <svg viewBox="0 0 14 12" aria-hidden="true"><path d="M1 4 C1 1 13 1 13 4 L11 5 L10 3.5 H4 L3 5 Z M3 6 H11 L12 11 H2 Z"/></svg>
        <span>(555) 314-2760</span>
      </div>
      <div class="contact-line">
        <svg viewBox="0 0 14 12" aria-hidden="true"><path d="M1 2 H13 V3 L7 7 L1 3 Z M1 4.5 L7 8.5 L13 4.5 V10 H1 Z"/></svg>
        <span>info@brennickholdings.com</span>
      </div>
    </div>
    <div class="web-rule">
      <span class="bullets"><i></i><i></i><i></i><i></i><i></i></span>
      <span class="rule rule-left"></span>
      <span>www.<strong>brennickholdings</strong>.com</span>
      <span class="rule rule-right"></span>
    </div>
  </section>
  <section class="card-back">
    <div class="back-pattern" role="img" aria-label="Dark navy card back with a repeated embossed brand pattern"></div>
    <p class="back-brand"><span class="ring"></span><span>Brennick Holdings</span></p>
  </section>
</main>
</body>
</html>
```